Net Clarity Partners Needs a New Business Card Design

Attached is my new logo that ArtFlockly created and picture of me for the back of the business card. Also attached is the information to include on the business card (on my existing business card design - NCP1 file attached).

The designer also provided a treatment of my logo that I really like if you can use it somehow. Also attached - file name "Preferred Version of New Logo."

Marla Quinteros

Net Clarity Partners
4817 Brindle Ave., #315
Houston, TX 77056

Tel: (832) 555-0147
www.netclaritypartners.example
marla@netclaritypartners.example

Thank you.

Target Market(s)

attorneys and law firms

Industry/Entity Type

Legal

Contact Information for Business Card

Proved in the Project Description

Font styles to use
Other font styles liked:
• I am open on font - no script though.

Colors
2d73b3
33a6d7

Requirements
Must have
• my logo
• company name & contact info
• my picture on the back
• colors that coordinate with the logo
Nice to have
• love to use the treated version of the logo if possible

```html
<!DOCTYPE html>
<html lang="en">
<head>
<meta charset="utf-8">
<title>Net Clarity Partners – Business Card</title>
<link rel="stylesheet" href="https://fonts.googleapis.com/css2?family=Open+Sans:wght@400;600;700&display=swap">
<style>
  :root {
    --page-bg: #e9e7e4;
    --card-white: #ffffff;
    --brand-blue: #33a6d7;
    --brand-deep: #2d73b3;
    --ink: #3b3f44;
    --ink-strong: #2e3135;
    --band-grey: #939598;
    --tag-grey: #8a8d91;
    --back-dark: #1c2830;
    --back-light: #374a54;
    --photo-top: #c9b7a4;
    --photo-mid: #8e7a6a;
    --photo-low: #3a3fa8;
  }
  * { margin: 0; padding: 0; box-sizing: border-box; }
  html, body {
    width: 1200px; height: 987px; overflow: hidden;
    background: var(--page-bg);
    font-family: "Open Sans", Arial, sans-serif;
  }
  .card {
    position: absolute; left: 293px; width: 615px; height: 350px;
    overflow: hidden;
    box-shadow: 0 6px 18px rgba(0,0,0,0.18);
  }
  .card-front { top: 130px; background: var(--card-white); }
  .card-back {
    top: 506px;
    background: radial-gradient(ellipse 70% 80% at 62% 30%, var(--back-light), var(--back-dark) 75%);
  }
  .brand-name {
    position: absolute; color: var(--brand-blue); font-weight: 700;
    letter-spacing: 0.5px; text-transform: uppercase; white-space: nowrap;
  }
  .brand-tagline {
    position: absolute; color: var(--tag-grey); font-weight: 700;
    text-transform: uppercase; white-space: nowrap;
  }
  .card-front .brand-name { left: 32px; top: 66px; font-size: 24px; }
  .card-front .brand-tagline { left: 33px; top: 98px; font-size: 8.5px; letter-spacing: 3.2px; }
  .person-name {
    position: absolute; left: 32px; top: 130px;
    font-size: 21px; font-weight: 600; color: var(--brand-blue);
    text-transform: uppercase;
  }
  .address { position: absolute; left: 32px; top: 166px; font-size: 15px; line-height: 22px; color: var(--ink); }
  .address .company { font-weight: 700; color: var(--ink-strong); }
  .contacts { position: absolute; left: 32px; top: 233px; list-style: none; font-size: 15px; color: var(--ink); }
  .contacts li { display: flex; align-items: center; height: 23.5px; }
  .contacts svg { width: 15px; height: 15px; margin-right: 10px; flex: none; }
  .portrait {
    position: absolute; left: 322px; top: 0; width: 293px; height: 320px;
    background: linear-gradient(180deg, var(--card-white) 0%, var(--photo-top) 12%, var(--photo-mid) 50%, var(--photo-low) 78%, var(--photo-low) 100%);
    clip-path: polygon(14% 100%, 22% 80%, 32% 62%, 34% 8%, 60% 2%, 80% 10%, 82% 55%, 100% 70%, 100% 100%);
  }
  .footer-band { position: absolute; left: 0; bottom: 0; width: 100%; height: 30px; background: var(--band-grey); }
  .card-back .brand-name { left: 0; width: 100%; text-align: center; top: 104px; font-size: 30px; }
  .card-back .brand-tagline { left: 0; width: 100%; text-align: center; top: 144px; font-size: 10px; letter-spacing: 4.5px; color: #a9adb1; }
  .social-row { position: absolute; top: 277px; left: 0; width: 100%; display: flex; justify-content: center; gap: 10px; }
  .social-row span { width: 20px; height: 20px; border-radius: 50%; background: var(--brand-blue); }
</style>
</head>
<body>
  <section class="card card-front">
    <div class="brand-name">Net Clarity Partners</div>
    <div class="brand-tagline">Smart marketing for law firms</div>
    <h1 class="person-name">Marla Quinteros</h1>
    <p class="address">
      <span class="company">Net Clarity Partners</span><br>
      4817 Brindle Ave., #315<br>
      Houston, TX 77056
    </p>
    <ul class="contacts">
      <li>
        <svg viewBox="0 0 16 16"><path fill="#33a6d7" d="M3.6 1.2l2.3 2.8-1.4 1.8c.9 2 2.6 3.7 4.6 4.6l1.8-1.4 2.8 2.3-1.2 2.4C7.4 14.2 1.8 8.6 1.2 2.4z"/></svg>
        (832) 555-0147
      </li>
      <li>
        <svg viewBox="0 0 16 16"><rect x="1" y="3.5" width="14" height="9.5" fill="#33a6d7"/><path d="M1.5 4l6.5 5 6.5-5" fill="none" stroke="#fff" stroke-width="1.2"/></svg>
        marla@netclaritypartners.example
      </li>
      <li>
        <svg viewBox="0 0 16 16"><circle cx="8" cy="8" r="7" fill="#33a6d7"/><path d="M1 8h14M8 1c-3 3-3 11 0 14M8 1c3 3 3 11 0 14" fill="none" stroke="#fff" stroke-width="1"/></svg>
        www.netclaritypartners.example
      </li>
    </ul>
    <div class="portrait" role="img" aria-label="Portrait photo of Marla Quinteros in a blue top"></div>
    <div class="footer-band"></div>
  </section>

  <section class="card card-back">
    <div class="brand-name">Net Clarity Partners</div>
    <div class="brand-tagline">Smart marketing for law firms</div>
    <div class="social-row" aria-label="Social profiles">
      <span></span><span></span><span></span><span></span><span></span>
    </div>
  </section>
</body>
</html>
```